Makeup Artist Requires Business Card design

Hi

I am looking for a business card design to market my makeup artist business. I operate under my own name Mara Veldt and I would like to keep the design of the card very simplistic and chic - something that keeps both my name and profession (makeup artist) the focus of the card. I would like it to be a style that is eyecatching to the reader (i am open to anything unusual) but upmarket.

Target Market(s)

women, magazine/beauty/fashion editors, photographers.

Industry/Entity Type

Business

Requirements
Must have
• Must contain:

Phone number: 0418 372 915
Website: www.maraveldt.com.au
email: contact@maraveldt.com.au

(although you don't need to have prefaced these with the words phone number, website etc :))
Should not have
• I am not looking for anything overly colorful - my preference is to keep the card dark if possible.

```html
<!DOCTYPE html>
<html lang="en">
<head>
<meta charset="utf-8">
<title>Mara Veldt – Makeup Artist Business Card</title>
<link rel="stylesheet" href="https://fonts.googleapis.com/css2?family=Arimo:wght@400&display=swap">
<style>
  :root {
    --paper: #ffffff;
    --card: #000000;
    --type: #ffffff;
    --accent: #f39c00;
    --echo: #6a6a6a;
    --label: #000000;
  }
  html, body {
    margin: 0;
    padding: 0;
    width: 1018px;
    height: 1200px;
    overflow: hidden;
    background: var(--paper);
  }
  .sheet {
    display: block;
    width: 1018px;
    height: 1200px;
    font-family: "Arimo", Arial, sans-serif;
  }
  .side-label {
    fill: var(--label);
    font-size: 50px;
    text-anchor: middle;
  }
  .card-face { fill: var(--card); }
  .profession { fill: var(--type); font-size: 165px; }
  .profession-echo { fill: var(--echo); font-size: 165px; }
  .divider { fill: var(--accent); }
  .name { fill: var(--type); font-size: 118px; }
  .contact { fill: var(--type); font-size: 24.5px; }
  .kiss-mark { fill: var(--accent); }
</style>
</head>
<body>
<svg class="sheet" viewBox="0 0 1190 1420" preserveAspectRatio="xMidYMid meet" xmlns="http://www.w3.org/2000/svg">
  <defs>
    <clipPath id="front-bounds">
      <rect x="123" y="108" width="1049" height="603"/>
    </clipPath>
  </defs>

  <!-- Front side -->
  <text class="side-label" x="615" y="46">FRONT</text>
  <g class="card card-front">
    <rect class="card-face" x="123" y="108" width="1049" height="603"/>
    <g clip-path="url(#front-bounds)">
      <text class="profession-echo" transform="translate(118,178) rotate(64)" textLength="545" lengthAdjust="spacingAndGlyphs">Makeup artist</text>
      <text class="profession" transform="translate(145,150) rotate(64)" textLength="545" lengthAdjust="spacingAndGlyphs">Makeup artist</text>

      <polygon class="divider" points="292,108 297,108 512,580 502,584"/>
    </g>

    <text class="name" x="548" y="470" textLength="600" lengthAdjust="spacingAndGlyphs">Mara Veldt</text>

    <g class="contact-block">
      <text class="contact" x="738" y="563">Phone number: 0418 372 915</text>
      <text class="contact" x="738" y="610">Website: www.maraveldt.com.au</text>
      <text class="contact" x="738" y="657">email: contact@maraveldt.com.au</text>
    </g>
  </g>

  <!-- Back side -->
  <text class="side-label" x="617" y="782">BACK</text>
  <g class="card card-back">
    <rect class="card-face" x="123" y="815" width="1045" height="599"/>
    <ellipse class="kiss-mark" role="img" aria-label="Orange lipstick kiss print" cx="918" cy="1213" rx="142" ry="92" transform="rotate(-12 918 1213)"/>
  </g>
</svg>
</body>
</html>
```